Company Mission & Values Poster

I'd like an A2 Portrait Poster displaying our company's Mission & Values.
See our website for our logo, fonts, mission & values.
https://talvendo.com.au/

Our Mission: Creating homes for abundant life
Values: Love, Thinking, Team, Zoe.

Some ideas to consider:
Mission as the Headline then
A logo for each of the 4 Values and the words

Target Market(s)

Myself & my team

Industry/Entity Type

Real Estate

Font styles to use
Other font styles liked:
• Company fonts as seen on our website

```html
<!DOCTYPE html>
<html lang="en">
<head>
<meta charset="utf-8">
<title>Talvendo – Mission &amp; Values Poster</title>
<link href="https://fonts.googleapis.com/css2?family=Lato:wght@700;900&family=Marcellus&family=Open+Sans:wght@400;700;800&display=swap" rel="stylesheet">
<style>
  :root {
    --forest: #0b3a30;
    --forest-glass: rgba(11, 58, 48, 0.93);
    --ink: #3b3b3d;
    --muted: #6d6d6d;
    --paper: #ffffff;
    --canvas: #2a2a2a;
  }
  * { margin: 0; padding: 0; box-sizing: border-box; }
  html, body { width: 881px; height: 1200px; overflow: hidden; background: var(--canvas); }
  .poster { position: relative; width: 881px; height: 1200px; background: var(--paper); overflow: hidden; }

  .hero-photo {
    position: absolute; left: 0; top: 0; width: 881px; height: 642px;
    background: linear-gradient(180deg, #ede7e3 0%, #e6dcd6 22%, #9fa6a6 33%, #6f7e70 40%, #4f5f44 50%, #a39d93 62%, #d5cdc5 80%, #bdb7b0 100%);
  }

  .mission-tab {
    position: absolute; left: 493px; top: 280px; width: 353px; height: 52px;
    background: var(--paper); border-top-right-radius: 18px;
    font: 800 36px/52px "Open Sans", sans-serif; color: var(--forest);
    padding-left: 24px; letter-spacing: -0.5px;
  }
  .mission-panel {
    position: absolute; left: 493px; top: 331px; width: 353px; height: 391px;
    background: var(--forest-glass); color: var(--paper); padding: 26px 24px 0;
  }
  .mission-statement { font-family: "Marcellus", serif; font-size: 50px; line-height: 59px; font-weight: 400; }
  .mission-statement strong { font-family: "Lato", sans-serif; font-weight: 900; font-size: 48px; }
  .mission-statement .rule { display: inline-block; width: 90px; height: 2px; background: var(--paper); vertical-align: middle; margin-left: 6px; }
  .mission-copy { margin-top: 22px; font: 400 13px/18.5px "Open Sans", sans-serif; }

  .values-tab {
    position: absolute; left: 0; top: 588px; width: 352px; height: 54px;
    background: var(--forest); border-top-right-radius: 18px;
    font: 800 34px/56px "Open Sans", sans-serif; color: var(--paper);
    padding-left: 52px; letter-spacing: -0.5px;
  }
  .values-headline {
    position: absolute; left: 56px; top: 660px; width: 800px;
    font: 700 33px/42px "Lato", sans-serif; color: var(--ink);
  }

  .value { position: absolute; top: 856px; width: 150px; }
  .value-badge { width: 120px; height: 120px; display: block; }
  .value-name { margin-top: 2px; font: 700 23px/30px "Lato", sans-serif; color: var(--forest); }
  .value-copy { font: 400 8.4px/12px "Open Sans", sans-serif; color: var(--muted); width: 146px; }
  .value--love { left: 52px; }
  .value--thinking { left: 269px; }
  .value--team { left: 484px; }
  .value--zoe { left: 691px; }

  .footer-band {
    position: absolute; left: 0; top: 1118px; width: 881px; height: 82px;
    background: var(--forest); display: flex; align-items: center; justify-content: center;
  }
  .brand-name { font: 400 46px/1 "Marcellus", serif; color: var(--paper); letter-spacing: 7px; }
</style>
</head>
<body>
<main class="poster">
  <div class="hero-photo" role="img" aria-label="Photo of a harbourside terrace with a stone dining table, woven chairs, palms and water at sunset"></div>

  <h2 class="mission-tab">OUR MISSION</h2>
  <section class="mission-panel">
    <h1 class="mission-statement">Creating<br><strong>Homes For</strong><br>Abundant<br>Life.<span class="rule"></span></h1>
    <p class="mission-copy">We wholeheartedly believe that home is an extraordinary place: a haven where life unfolds in all its glory. Where we find solace, make cherished memories with loved ones, and savour the natural beauty that surrounds us.</p>
  </section>

  <h2 class="values-tab">OUR VALUES</h2>
  <p class="values-headline">We Believe<br>Business Can Be A<br>Force For Good. Our Values Shape The Way We Work And How We Make Decisions.</p>

  <article class="value value--love">
    <svg class="value-badge" viewBox="0 0 120 120" aria-hidden="true">
      <circle cx="60" cy="60" r="60" fill="var(--forest)"/>
      <circle cx="60" cy="60" r="52" fill="none" stroke="#fff" stroke-width="1.5"/>
      <path d="M50 78 C28 62 32 44 42 44 C47 44 50 48 50 51 C50 48 53 44 58 44 C68 44 72 62 50 78Z" fill="#fff"/>
      <path d="M70 84 C50 70 54 54 63 54 C67 54 70 57 70 60 C70 57 73 54 77 54 C86 54 90 70 70 84Z" fill="#fff" stroke="var(--forest)" stroke-width="2.5"/>
    </svg>
    <h3 class="value-name">Love</h3>
    <p class="value-copy">Our mission is founded in our love and respect for people - those we develop for, those in our teams and those in the communities we create and operate within.</p>
  </article>

  <article class="value value--thinking">
    <svg class="value-badge" viewBox="0 0 120 120" aria-hidden="true">
      <circle cx="60" cy="60" r="60" fill="var(--forest)"/>
      <circle cx="60" cy="60" r="52" fill="none" stroke="#fff" stroke-width="1.5"/>
      <g fill="none" stroke="#fff" stroke-width="2.2" stroke-linejoin="round">
        <path d="M48 86 L48 76 C38 72 34 62 37 52 C40 40 52 34 64 36 C76 38 84 48 82 60 L86 68 L81 69 L81 76 C81 80 78 81 74 81 L70 81 L70 86"/>
        <circle cx="62" cy="56" r="8"/>
        <circle cx="62" cy="56" r="3"/>
        <path d="M62 44v4M62 64v4M50 56h4M70 56h4M54 48l3 3M67 61l3 3M70 48l-3 3M54 64l3-3"/>
      </g>
    </svg>
    <h3 class="value-name">Thinking</h3>
    <p class="value-copy">We believe in the power of thinking. Our rigorous and creative processes create beautifully considered solutions for our purchasers, the communities we develop within and the environment.</p>
  </article>

  <article class="value value--team">
    <svg class="value-badge" viewBox="0 0 120 120" aria-hidden="true">
      <circle cx="60" cy="60" r="60" fill="var(--forest)"/>
      <circle cx="60" cy="60" r="52" fill="none" stroke="#fff" stroke-width="1.5"/>
      <g fill="#fff">
        <circle cx="60" cy="38" r="7"/><circle cx="45" cy="42" r="6"/><circle cx="75" cy="42" r="6"/>
        <path d="M36 58 C36 50 42 48 46 48 C49 48 51 49 52 50 C55 47 57 46 60 46 C63 46 65 47 68 50 C69 49 71 48 74 48 C78 48 84 50 84 58Z"/>
      </g>
      <path d="M36 62 H84 L86 66 L80 70 L82 76 L76 78 L74 84 L68 82 L64 87 L60 84 L56 87 L52 82 L46 84 L44 78 L38 76 L40 70 L34 66Z M50 64 A10 10 0 0 0 70 64Z" fill="#fff" fill-rule="evenodd"/>
    </svg>
    <h3 class="value-name">Team</h3>
    <p class="value-copy">Property development is a team sport. We surround ourselves with the best designers and advisers. We strive to create an environment that allows them to do their best work and love doing it.</p>
  </article>

  <article class="value value--zoe">
    <svg class="value-badge" viewBox="0 0 120 120" aria-hidden="true">
      <circle cx="60" cy="60" r="60" fill="var(--forest)"/>
      <circle cx="60" cy="60" r="52" fill="none" stroke="#fff" stroke-width="1.5"/>
      <g fill="none" stroke="#fff" stroke-width="2.4" stroke-linejoin="round">
        <path d="M32 56 L58 32 L84 56"/>
        <path d="M40 50 V86 H66"/>
        <path d="M78 50 V62"/>
        <rect x="50" y="62" width="12" height="24"/>
        <path d="M55 44 L58 41 L61 44 L58 47Z"/>
        <path d="M68 86 L86 68 V86Z"/>
      </g>
    </svg>
    <h3 class="value-name">Zoe</h3>
    <p class="value-copy">Our mission is to create places for 'Zoe' - the Greek word for abundant life. We do this through exquisite design, quality construction and celebrating nature.</p>
  </article>

  <footer class="footer-band">
    <span class="brand-name">TALVENDO</span>
  </footer>
</main>
</body>
</html>
```